Van wrap design for Kolvane Tramline long wheelbase high top 2017 model for Ashvale Garden Studios

We are a garden Studio manufacturer and need a great looking van wrap for a Kolvane Tramline long wheel base high top 2017 model somehow using our logo and the photos of our Studio supplied.

There are a few photos to use but our favourite is DSC_0481 Friday, 06 October 2017 18:42:16, so could you try a few different designs using all photos and a few different designs using just our favourite photo.

We leave the design to you with us only asking one thing, to have our logo on the bonnet. As we are a high-quality company we want this to reflect on the design, ie, not a cheap looking wrap.

The van is White but would like the van fully wrapped Black with the design covering it.

Target Market(s)

High end clients

Industry/Entity Type

Wheel

Font styles to use
Other font styles liked:
• To suit our Logo

Colors

Designer to choose colors to be used in the design.

Requirements
Must have
• Logo on bonnet
• these details somewhere looking good:
• Website: www.ashvalegardenstudios.co.uk
• Address: Unit 4, Pellow Yard, Dunscombe, Ashgrove, PL22 9QT
• phone: 01632 960482
• Email: ashvalegardenstudios@mailvista.co.uk

```html
<!DOCTYPE html>
<html lang="en">
<head>
<meta charset="utf-8">
<title>Ashvale Garden Studios – Van Wrap</title>
<link rel="stylesheet" href="https://fonts.googleapis.com/css2?family=Ubuntu:wght@500;700&family=Open+Sans:wght@400&display=swap">
<style>
  :root {
    --wrap-black: #121214;
    --brand-green: #2fae6a;
    --text-white: #f4f4f4;
    --page: #ffffff;
    --foliage-dark: #26361f;
    --foliage-mid: #4f6a3a;
    --studio-stone: #6e6a64;
    --glow: #d8b88a;
    --badge: #2a2a2a;
  }
  * { margin: 0; padding: 0; box-sizing: border-box; }
  html, body { width: 1200px; height: 1179px; overflow: hidden; background: var(--page); }
  .canvas { position: relative; width: 1200px; height: 1179px; font-family: "Ubuntu", sans-serif; }

  .panel { position: absolute; background: var(--wrap-black); overflow: hidden; }
  .panel--side { left: 20px; top: 75px; width: 1145px; height: 415px; border-radius: 90px 60px 30px 30px; }
  .panel--front { left: 30px; top: 555px; width: 570px; height: 600px; border-radius: 120px 120px 40px 40px; }
  .panel--rear { left: 655px; top: 560px; width: 505px; height: 595px; border-radius: 70px 70px 30px 30px; }

  .t { position: absolute; white-space: nowrap; }
  .brand-name { font-family: "Ubuntu", sans-serif; font-weight: 700; color: var(--brand-green); text-transform: uppercase; line-height: 1; }
  .brand-sub { font-family: "Ubuntu", sans-serif; font-weight: 700; color: var(--brand-green); text-transform: uppercase; line-height: 1; letter-spacing: 0.04em; }
  .web { font-family: "Open Sans", sans-serif; color: var(--brand-green); line-height: 1; }
  .mail { font-family: "Open Sans", sans-serif; color: var(--text-white); line-height: 1; }
  .phone { font-family: "Ubuntu", sans-serif; font-weight: 700; line-height: 1; letter-spacing: 0.04em; }
  .address { font-family: "Ubuntu", sans-serif; font-weight: 700; color: var(--brand-green); line-height: 1; }

  .studio-photo {
    position: absolute;
    background: linear-gradient(100deg, var(--foliage-dark) 0%, var(--foliage-mid) 22%, var(--studio-stone) 45%, var(--glow) 60%, var(--studio-stone) 75%, var(--foliage-dark) 100%);
    border-top: 3px solid var(--text-white);
    clip-path: polygon(0 6%, 6% 2%, 12% 7%, 19% 1%, 27% 6%, 34% 2%, 42% 8%, 50% 3%, 58% 7%, 66% 1%, 74% 6%, 82% 2%, 90% 7%, 100% 3%, 100% 100%, 0 100%);
  }
  .dealer-badge { position: absolute; background: var(--badge); border-radius: 6px; }
</style>
</head>
<body>
<main class="canvas">

  <section class="panel panel--side" aria-label="Side view wrap">
    <div class="t brand-name" style="left:390px; top:28px; font-size:76px; letter-spacing:0.05em;">Ashvale</div>
    <div class="t brand-sub" style="left:520px; top:108px; font-size:32px;">Garden Studios</div>
    <div class="t web" style="left:368px; top:145px; font-size:21px;">www.ashvalegardenstudios.co.uk</div>
    <div class="t mail" style="left:368px; top:172px; font-size:12px;">ashvalegardenstudios@mailvista.co.uk</div>
    <div class="t phone" style="left:872px; top:146px; font-size:22px; color:var(--brand-green);">01632 960482</div>
    <div class="studio-photo" role="img" aria-label="Garden studio with glass doors among planting" style="left:170px; top:190px; width:975px; height:225px;"></div>
    <div class="t address" style="left:235px; top:346px; font-size:18px;">Unit 4, Pellow Yard, Dunscombe, Ashgrove, PL22 9QT</div>
  </section>

  <section class="panel panel--front" aria-label="Front view wrap with logo on bonnet">
    <div class="t brand-name" style="left:0; width:570px; text-align:center; top:20px; font-size:46px; letter-spacing:0.05em;">Ashvale</div>
    <div class="t brand-sub" style="left:0; width:570px; text-align:center; top:72px; font-size:16px;">Garden Studios</div>
    <div class="t web" style="left:0; width:570px; text-align:center; top:96px; font-size:17px;">www.ashvalegardenstudios.co.uk</div>
    <div class="studio-photo" role="img" aria-label="Garden studio among shrubs" style="left:100px; top:235px; width:345px; height:105px;"></div>
  </section>

  <section class="panel panel--rear" aria-label="Rear view wrap">
    <div class="t phone" style="left:0; width:505px; text-align:center; top:58px; font-size:30px; color:var(--text-white);">01632 960482</div>
    <div class="t brand-name" style="left:0; width:505px; text-align:center; top:110px; font-size:50px; letter-spacing:0.05em;">Ashvale</div>
    <div class="t brand-sub" style="left:0; width:505px; text-align:center; top:168px; font-size:20px;">Garden Studios</div>
    <div class="t address" style="left:0; width:505px; text-align:center; top:208px; font-size:13px;">Unit 4, Pellow Yard, Dunscombe, Ashgrove, PL22 9QT</div>
    <div class="t mail" style="left:0; width:505px; text-align:center; top:238px; font-size:17px;">ashvalegardenstudios@mailvista.co.uk</div>
    <div class="t web" style="left:0; width:505px; text-align:center; top:264px; font-size:20px;">www.ashvalegardenstudios.co.uk</div>
    <div class="studio-photo" role="img" aria-label="Garden studio with open door and planting" style="left:20px; top:330px; width:465px; height:265px;"></div>
    <div class="dealer-badge" style="left:75px; top:512px; width:140px; height:32px;"></div>
  </section>

</main>
</body>
</html>
```